Stationary and business cards for TerraQuestia-an Education, Enrichment, and Conservation Ctr
TerraQuestia (top line) Education, Enrichment, Conservation
Stationary and business cards for TerraQuestia-an Education, Enrichment, and Conservation Ctr - Animals
Creative Brief
Bright & Fun-filled
Tova Ruth Kellerby-Doane
Executive Director
483 Brindwick Rd. suite 300 Ostervale, MD 20947
tovark@mailcove.example
www.TerraQuestia.example
I would like it to have foliage or vines coming out of the sides like rainforest...maybe a red eye tree frog somewhere and a morpho butterfly... Want it to be simple but classy....and want to be able to have the names and contact info to be interchangeable for all my employees. For the stationary I want the logo somewhere as well. Thank you!
The logo
tovark tovark
I like the leaf addition, but instead of putting it in the back...can you replace the lines in the front of the business card and putting the leaf outlines? That goes better with our theme than "professional" looking lines etc.... thanks!
I can't find how to attach the logo?
quintonhalvard7314065 quintonhalvard7314065
i need the logo logo are not attach in Brief
you can go to our website to get an idea of who we are www.TerraQuestia.example and see our logo.

```html
<!DOCTYPE html>
<html lang="en">
<head>
<meta charset="utf-8">
<title>TerraQuestia Business Cards</title>
<link href="https://fonts.googleapis.com/css2?family=Open+Sans:wght@400;600;700;800&display=swap" rel="stylesheet">
<style>
  :root {
    --backdrop: #e9e7e3;
    --card: #ffffff;
    --olive: #6e5c1f;
    --olive-dark: #4f4214;
    --leaf: #4e7a2a;
    --ink: #3a3528;
    --back-text: #efe7cf;
    --silver-light: #f2f2f2;
    --silver-mid: #b9b9b9;
    --silver-dark: #8a8a8a;
  }
  * { margin: 0; padding: 0; box-sizing: border-box; }
  html, body {
    width: 1200px; height: 909px; overflow: hidden;
    background: var(--backdrop);
    font-family: "Open Sans", Arial, sans-serif;
  }
  .canvas { position: relative; width: 1200px; height: 909px; }
  .card {
    position: absolute; top: 115px;
    width: 420px; height: 680px;
    background: var(--card);
    overflow: hidden;
    box-shadow: 0 6px 22px rgba(0,0,0,0.18);
  }
  .card--front { left: 150px; }
  .card--back { left: 630px; }
  .card-art { position: absolute; inset: 0; width: 100%; height: 100%; }

  .brand {
    position: absolute; left: 0; right: 0; top: 70px;
    display: flex; flex-direction: column; align-items: center;
  }
  .brand-line { display: flex; align-items: center; gap: 10px; }
  .brand-dot { width: 18px; height: 18px; border-radius: 50%; background: var(--leaf); }
  .brand-name {
    font-weight: 800; font-size: 40px; color: var(--leaf);
    letter-spacing: 0.5px; line-height: 1;
  }
  .brand-tagline {
    margin-top: 8px; font-size: 11px; color: var(--olive);
    letter-spacing: 0.6px;
  }

  .contact {
    position: absolute; left: 140px; top: 410px; width: 260px;
    color: var(--ink); font-size: 14px; line-height: 1.45;
  }
  .contact-name { font-weight: 700; font-size: 17px; color: var(--olive-dark); white-space: nowrap; }
  .contact-role { font-size: 15px; margin-bottom: 14px; }
  .contact-address { margin-bottom: 12px; }
  .contact-label { font-weight: 700; color: var(--olive); }
  .contact-web { margin-top: 12px; }

  .back-web {
    position: absolute; right: 26px; bottom: 150px;
    writing-mode: vertical-rl;
    transform: rotate(180deg);
    color: var(--back-text); font-size: 12px; letter-spacing: 0.4px;
    white-space: nowrap;
  }
</style>
</head>
<body>
<main class="canvas">

  <section class="card card--front" aria-label="Business card front">
    <svg class="card-art" viewBox="0 0 420 680" aria-hidden="true">
      <defs>
        <linearGradient id="silverSweep" x1="0" y1="0" x2="1" y2="0">
          <stop offset="0" stop-color="#f2f2f2"/>
          <stop offset="0.45" stop-color="#8a8a8a"/>
          <stop offset="1" stop-color="#b9b9b9"/>
        </linearGradient>
      </defs>
      <path d="M0 395 Q 180 285 420 262 L420 290 Q 200 300 0 418 Z" fill="url(#silverSweep)"/>
      <path d="M0 418 Q 200 300 420 290" fill="none" stroke="#dcdcdc" stroke-width="2"/>
    </svg>
    <div class="brand">
      <div class="brand-line">
        <span class="brand-dot"></span>
        <span class="brand-name">TerraQuestia</span>
      </div>
      <div class="brand-tagline">Education • Enrichment • Conservation</div>
    </div>
    <div class="contact">
      <div class="contact-name">Tova Ruth Kellerby-Doane</div>
      <div class="contact-role">Consultant</div>
      <div class="contact-address">483 Brindwick Rd. suite 300<br>Ostervale, MD 20947</div>
      <div><span class="contact-label">Ph:</span> 555 014 2290</div>
      <div><span class="contact-label">Cell:</span> 555 014 2291</div>
      <div><span class="contact-label">Fax:</span> 555 014 2292</div>
      <div><span class="contact-label">Email:</span> tovark@mailcove.example</div>
      <div class="contact-web">www.TerraQuestia.example</div>
    </div>
  </section>

  <section class="card card--back" aria-label="Business card back">
    <svg class="card-art" viewBox="0 0 420 680" aria-hidden="true">
      <defs>
        <linearGradient id="silverRim" x1="0" y1="0" x2="1" y2="0">
          <stop offset="0" stop-color="#f2f2f2"/>
          <stop offset="0.5" stop-color="#8a8a8a"/>
          <stop offset="1" stop-color="#b9b9b9"/>
        </linearGradient>
      </defs>
      <path d="M0 330 Q 230 350 420 190 L420 680 L0 680 Z" fill="url(#silverRim)"/>
      <path d="M0 346 Q 235 362 420 208 L420 680 L0 680 Z" fill="#6e5c1f"/>
    </svg>
    <div class="brand">
      <div class="brand-line">
        <span class="brand-dot"></span>
        <span class="brand-name">TerraQuestia</span>
      </div>
      <div class="brand-tagline">Education • Enrichment • Conservation</div>
    </div>
    <div class="back-web">www.TerraQuestia.example</div>
  </section>

</main>
</body>
</html>
```